依頼詳細
<サイトマップ>
①TOPページ
②SALON(店舗情報)
③STAFF(スタッフ紹介)
④STYLE(ギャラリー)
⑤COUPON(クーポン)
⑥FEATURE(当店の特徴)
⑦RECRUIT/COMPANY(求人・会社概要)
⑧BLOG(サイト内ブログ)
⑨NEWS(サイト内ブログ)
⑩MENU(メニュー)
⑪VOICE(お客様の声)
⑫GUEST SNAP(ゲストスナップ)

<デザインテイスト>
・ナチュラル  ・優しい  ・モダン  ・清潔な

<顧客ターゲット>
・女性
・20代~50代
①40代 ②50代 ③20代
・学生、会社員、自営業、未婚、既婚、妊婦、子育て、中年

【競合サイト】
http://www.tintomopalor.j(大阪中心のカラー専門サロン)
http://www.brisk-lumen.j(大きいサロン)
http://www.vexo-rud.co (北海道で大きいサロン)

【要望】
・pinquorのアイコンをサイト内に配置してください。
・予約が外部のためバナーなどを配置して頂けると嬉しいです。
・「VOICE」ページにはA4サイズのカウンセリングシートなどを
お客様に記入していただいたものを添付する予定ですので、TOpに
新着エリアなどがあってもうれしいです。
・ブログ、新着は新着BOXで配置して頂きたいです。

※素材は追記分内に書いています。
水色系
【素材】
■ミルカノ
素材として定期ダウンロードできる画像は使用して頂いて構いません。
その際にカンプ画像でダウンロードしてください。
(画像検索した際に出てくるサムネール下の画像番号の横にミルカノのマーク
があるものは使用不可できません・・・)
その他の素材に関しては、フリーで提供可能なものでお願いします。
■サロン外観・内装写真(ロゴ入り)
http://quolbank.jp/download/e3f7c2a9d81b04f65e2c7a93d0b1f48e27cd5a16
ダウンロードパスワード ruqwept4

すみません、ミルカノのURL添付し忘れてました。
https://jp.mirkano.com/

宜しくお願いします。
今回、当サロンのコンペに閲覧・ご提案して頂きましたデザイナー様
誠にありがとうございます!!
今でもたくさんのデザイン案を提案して頂いておりますが、もう少し色々なデザイン案を見たいという事もあり、1週間コンペ期間を延長することと致しました。
依頼詳細に囚われず、色みやレイアウトもデザイナー様の自由にデザインして頂いたものをみたいので是非、提案頂ければとても嬉しいです!!
(できれば、入れて頂くページは変えないでほしいです。)
どうぞ、宜しくお願い致します。

シンプルな中にも細部までの細やかなデザインや、デザイナー様のセンスの良さもあってサロンにとてもあったデザインに仕上がっていると思います。
とても満足しています。

今回ご提案していただいたデザイナー様へ
たくさんのデザイン案を度提案頂きまして、誠にありがとうございました。
”カラー専門店”という少し珍しい業態で当サロンの良さをうまく取り入れてくださっている方が多い中で一つに絞るのが中々、大変ではありました。
どれももったいないデザインばかりでした。。。
またこのような機会がございましたら是非ご提案していただければ幸いでございます。
ありがとうございました。

```html
<!DOCTYPE html>
<html lang="ja">
<head>
<meta charset="utf-8">
<title>Miravel ヘアカラー専門サロン</title>
<link rel="stylesheet" href="https://fonts.googleapis.com/css2?family=Noto+Sans+JP:wght@400;700&family=Noto+Serif+JP:wght@500&family=Cormorant+Garamond:ital,wght@1,600&display=swap">
<style>
:root{
  --bg:#e9e9e9;
  --panel:#ffffff;
  --line:#d6d6d6;
  --ink:#555555;
  --soft:#8d8d8d;
  --aqua:#6fc3d6;
  --aqua-pale:#dff2f7;
  --pink:#e96d9f;
  --lime:#b6d66a;
  --dark:#3a3a3a;
  --photo-a:#d9c2ad;
  --photo-b:#b79a84;
}
*{box-sizing:border-box;margin:0;padding:0}
html,body{width:805px;height:1200px;overflow:hidden}
body{background:var(--bg);font-family:"Noto Sans JP",sans-serif;color:var(--ink);position:relative;font-size:9px}
.abs{position:absolute}
.photo{background:linear-gradient(135deg,var(--photo-a),var(--photo-b))}

.header{left:0;top:0;width:805px;height:64px;background:var(--panel);border-bottom:1px solid var(--line)}
.logo{left:22px;top:20px;display:flex;align-items:center;gap:6px;font-family:"Cormorant Garamond",serif;font-style:italic;font-weight:600;font-size:20px;color:var(--soft)}
.logo-dot{width:12px;height:12px;border-radius:50%;background:var(--aqua-pale);border:1px solid var(--aqua)}
.nav{left:120px;top:27px;display:flex;gap:18px;font-size:9px;letter-spacing:.05em;color:var(--soft)}
.nav .on{color:var(--aqua)}
.util{left:560px;top:6px;width:235px;font-size:7px;color:var(--soft)}
.util-row{display:flex;align-items:center;gap:8px;margin-top:5px}
.btn-reserve{background:var(--pink);color:#fff;font-size:8px;padding:3px 10px;border-radius:2px}
.tel{font-size:11px;color:var(--aqua);font-weight:700}
.sns{display:flex;align-items:center;gap:4px;color:var(--aqua);font-size:9px}
.sns i{width:10px;height:10px;background:var(--aqua);display:block}

.box{background:var(--panel);border:1px solid var(--line)}
.hero{left:125px;top:76px;width:555px;height:258px}
.hero-photo{left:8px;top:8px;width:200px;height:232px}
.hero-copy{left:225px;top:26px;width:315px}
.hero-copy h1{font-family:"Noto Serif JP",serif;font-weight:500;font-size:13px;color:var(--ink);text-align:center}
.hero-copy h1 em{font-style:normal;font-size:17px;color:var(--aqua)}
.hero-copy p{margin-top:14px;font-size:8px;line-height:1.9;color:var(--soft)}
.dots{left:14px;top:244px;display:flex;gap:4px}
.dots i{width:6px;height:6px;border-radius:50%;background:#ccc;display:block}
.dots i:first-child{background:var(--aqua)}

.ttl{font-family:"Cormorant Garamond",serif;font-style:italic;font-weight:600;font-size:15px;color:var(--soft);text-align:center;padding-top:6px}
.ttl::after{content:"";display:block;width:60px;height:1px;background:var(--aqua);margin:3px auto 0}

.news{left:125px;top:346px;width:325px;height:250px}
.news-list{list-style:none;padding:8px 12px}
.news-item{display:flex;gap:8px;padding:6px 0;border-bottom:1px dotted var(--line);height:48px}
.news-thumb{width:36px;height:36px;border-radius:50%;flex:none}
.news-body{flex:1}
.news-head{display:flex;justify-content:space-between;font-size:8px;font-weight:700}
.tag{font-weight:400;font-size:7px;color:#fff;background:var(--lime);padding:0 6px;border-radius:6px}
.tag.blog{background:var(--aqua)}
.news-body p{font-size:7px;color:var(--soft);margin-top:3px;line-height:1.5}

.snap{left:460px;top:346px;width:220px;height:250px}
.snap-photo{left:12px;top:36px;width:110px;height:170px}
.snap-text{left:130px;top:40px;width:80px;font-size:7px;line-height:1.7;color:var(--soft)}
.snap-name{left:12px;top:214px;font-size:8px;font-weight:700}

.style{left:125px;top:606px;width:325px;height:120px}
.style-row{display:flex;gap:8px;padding:10px 12px}
.style-row div{width:54px;height:66px;border-radius:4px}

.voice{left:460px;top:606px;width:220px;height:230px}
.voice-list{list-style:none;padding:8px 12px}
.voice-item{display:flex;gap:8px;height:46px;border-bottom:1px dotted var(--line);padding-top:5px}
.voice-item .av{width:30px;height:30px;border-radius:50%;flex:none;background:var(--aqua-pale);border:1px solid var(--aqua)}
.voice-item b{font-size:8px;display:block}
.voice-item span{font-size:7px;color:var(--soft)}

.offer{left:125px;top:740px;width:325px;height:92px;background:var(--panel);border:1px solid var(--line)}
.offer-art{left:10px;top:10px;width:70px;height:72px;background:linear-gradient(180deg,var(--aqua-pale),#f6dbe6)}
.offer-bubble{left:92px;top:8px;width:222px;height:76px;border:2px solid var(--aqua);border-radius:38px;text-align:center;padding-top:10px}
.offer-bubble h3{font-size:10px;color:var(--aqua);font-weight:700}
.offer-bubble p{font-size:7px;color:var(--pink);margin-top:4px}
.offer-bubble span{display:inline-block;margin-top:5px;background:var(--pink);color:#fff;font-size:7px;padding:2px 12px;border-radius:8px}

.coupon{left:125px;top:842px;width:325px;height:72px;background:var(--aqua-pale);border:2px dashed var(--aqua);text-align:center;padding-top:10px}
.coupon small{font-family:"Cormorant Garamond",serif;font-style:italic;font-weight:600;font-size:13px;color:var(--aqua);letter-spacing:.1em}
.coupon p{font-size:15px;font-weight:700;color:var(--aqua);margin-top:2px}
.coupon p em{font-style:normal;color:var(--pink)}

.access{left:125px;top:924px;width:325px;height:122px}
.access-info{left:8px;top:6px;font-size:7px;color:var(--soft)}
.map{left:8px;top:22px;width:309px;height:92px;background:linear-gradient(135deg,#eef0e8,#dfe6ea)}
.pin{left:150px;top:45px}

.feed{left:460px;top:846px;width:220px;height:200px;background:var(--dark);color:#ddd}
.feed-head{padding:6px 8px;font-size:8px;font-weight:700;background:#2c2c2c;display:flex;gap:5px;align-items:center}
.feed-head i{width:9px;height:9px;background:var(--aqua);display:block}
.feed-post{display:flex;gap:6px;padding:8px;border-bottom:1px solid #555}
.feed-post .av{width:22px;height:22px;background:#777;flex:none}
.feed-post p{font-size:7px;line-height:1.5}

.sitemap{left:0;top:1066px;width:805px;height:94px;background:#d3d3d3}
.sitemap h2{font-family:"Cormorant Garamond",serif;font-style:italic;font-weight:600;font-size:14px;color:var(--aqua);text-align:center;padding-top:12px}
.footer{left:0;top:1160px;width:805px;height:40px;background:var(--dark);display:flex;justify-content:center;align-items:center;gap:16px;font-size:8px;color:#eee;letter-spacing:.05em}
</style>
</head>
<body>

<header class="abs header">
  <div class="abs logo"><i class="logo-dot"></i>Miravel</div>
  <nav class="abs nav">
    <span>TOP</span><span>SALON</span><span class="on">STYLE</span><span>MENU</span><span>STAFF</span><span>COUPON</span><span>VOICE</span><span>RECRUIT/COMPANY</span>
  </nav>
  <div class="abs util">
    ヘアカラー専門サロン｜やさしい薬剤で髪と頭皮をいたわります
    <div class="util-row">
      <span class="btn-reserve">ご予約はこちら</span>
      <span class="tel">0120-555-014</span>
      <span class="sns"><i></i>pinquor</span>
    </div>
  </div>
</header>

<section class="abs box hero">
  <div class="abs photo hero-photo" role="img" aria-label="柔らかなカラーのボブヘアの女性の写真"></div>
  <div class="abs hero-copy">
    <h1>毎日綺麗な髪であり続ける為に<em>髪と心のWケア</em></h1>
    <p>カラー専門サロンとして、髪と頭皮にやさしい薬剤を選び、お一人ひとりの肌色や雰囲気に合わせた色をご提案します。忙しい毎日の中でも気軽に通える、心地よい空間とていねいなカウンセリングで、あなたらしい美しさを引き出します。</p>
  </div>
  <div class="abs dots"><i></i><i></i><i></i><i></i></div>
</section>

<section class="abs box news">
  <h2 class="ttl">News &amp; Blog</h2>
  <ul class="news-list">
    <li class="news-item"><div class="news-thumb photo" role="img" aria-label="記事のサムネイル写真"></div><div class="news-body"><div class="news-head">記事タイトルが入ります<span class="tag">NEWS</span></div><p>記事の本文が入ります。記事の本文が入ります。記事の本文が入ります。</p></div></li>
    <li class="news-item"><div class="news-thumb photo" role="img" aria-label="記事のサムネイル写真"></div><div class="news-body"><div class="news-head">記事タイトルが入ります<span class="tag blog">BLOG</span></div><p>記事の本文が入ります。記事の本文が入ります。記事の本文が入ります。</p></div></li>
    <li class="news-item"><div class="news-thumb photo" role="img" aria-label="記事のサムネイル写真"></div><div class="news-body"><div class="news-head">記事タイトルが入ります<span class="tag">NEWS</span></div><p>記事の本文が入ります。記事の本文が入ります。記事の本文が入ります。</p></div></li>
    <li class="news-item"><div class="news-thumb photo" role="img" aria-label="記事のサムネイル写真"></div><div class="news-body"><div class="news-head">記事タイトルが入ります<span class="tag blog">BLOG</span></div><p>記事の本文が入ります。記事の本文が入ります。記事の本文が入ります。</p></div></li>
  </ul>
</section>

<section class="abs box snap">
  <h2 class="ttl">Guest Snap</h2>
  <div class="abs photo snap-photo" role="img" aria-label="ゲストのヘアスタイル写真"></div>
  <p class="abs snap-text">透明感のあるアッシュカラーで、春らしく軽やかな印象に仕上げました。</p>
  <p class="abs snap-name">ゲスト様 20代</p>
</section>

<section class="abs box style">
  <h2 class="ttl">Style</h2>
  <div class="style-row">
    <div class="photo" role="img" aria-label="ヘアスタイル写真1"></div>
    <div class="photo" role="img" aria-label="ヘアスタイル写真2"></div>
    <div class="photo" role="img" aria-label="ヘアスタイル写真3"></div>
    <div class="photo" role="img" aria-label="ヘアスタイル写真4"></div>
    <div class="photo" role="img" aria-label="ヘアスタイル写真5"></div>
  </div>
</section>

<section class="abs box voice">
  <h2 class="ttl">Voice</h2>
  <ul class="voice-list">
    <li class="voice-item"><i class="av"></i><div><b>40代 会社員</b><span>色持ちが良く大満足です。</span></div></li>
    <li class="voice-item"><i class="av"></i><div><b>50代 主婦</b><span>白髪も自然に染まりました。</span></div></li>
    <li class="voice-item"><i class="av"></i><div><b>20代 学生</b><span>丁寧な説明で安心でした。</span></div></li>
    <li class="voice-item"><i class="av"></i><div><b>30代 子育て中</b><span>短時間で通えて助かります。</span></div></li>
  </ul>
</section>

<section class="abs offer">
  <div class="abs offer-art" role="img" aria-label="カラーリストの女性のイラスト"></div>
  <div class="abs offer-bubble">
    <h3>カラーリストによる“今月の提案”</h3>
    <p>季節に合わせたおすすめカラーをご紹介</p>
    <span>詳しくはこちら</span>
  </div>
</section>

<section class="abs coupon">
  <small>COUPON</small>
  <p>クーポンご利用で<em>おトク</em>にキレイに!!</p>
</section>

<section class="abs box access">
  <p class="abs access-info">〒106-0000 東京都港区青葉台1-2-3 ｜ TEL 0120-555-014</p>
  <div class="abs map" role="img" aria-label="サロン周辺の地図"></div>
  <svg class="abs pin" width="14" height="20" viewBox="0 0 14 20"><path d="M7 0C3 0 0 3 0 7c0 5 7 13 7 13s7-8 7-13c0-4-3-7-7-7z" fill="#e96d9f"/><circle cx="7" cy="7" r="2.5" fill="#fff"/></svg>
</section>

<aside class="abs feed">
  <div class="feed-head"><i></i>pinquor</div>
  <div class="feed-post"><i class="av"></i><p>新しいカラー剤が入荷しました。ぜひお試しください。</p></div>
  <div class="feed-post"><i class="av"></i><p>今週末のご予約はまだ空きがございます。</p></div>
  <div class="feed-post"><i class="av"></i><p>春のおすすめカラー特集を公開しました。</p></div>
</aside>

<section class="abs sitemap"><h2>Site Map</h2></section>
<footer class="abs footer">
  <span>TOP</span><span>SALON</span><span>STAFF</span><span>STYLE</span><span>COUPON</span><span>FEATURE</span><span>RECRUIT/COMPANY</span><span>BLOG</span><span>NEWS</span><span>MENU</span><span>VOICE</span><span>GUEST SNAP</span>
</footer>

</body>
</html>
```